KORVa: AI driven decarbonization application

We are seeking an engaging, user-friendly, and visually appealing user interface for our B2B SaaS platform, Brelmont KORVa. This solution helps large organizations achieve net-zero emissions using AI-driven forecasting, AI models, a emission mitigation library, and a scenario simulator..

A big challenge is to allow the user to work efficiently with multidimensional data.

Requirements:

* Design a modern, professional, and visually striking user interface, catering to a diverse audience within large corporations, including executives, strategists, and environmental specialists.

* Construct an intuitive navigation system, allowing users to seamlessly access functionalities for informed decision-making and tracking progress towards net-zero emissions.

* The application is expected to be used on desktops first

* Incorporate our brand's colors, and visual elements into the design to maintain consistency throughout the application.

* Provide design assets and documentation, such as style guides, design specifications, and necessary assets (e.g., icons, illustrations) for our development team to implement the design. We use Figma and would appreciate delivery as figma files.

Please note that we also need more pages over time. The most important is to get the work bench page right. We will also need:
* a landing page where the users can select previous scenarios and see some high level data.
* A page with information on historical data per asset
* An analytics page
* User and system administration pages.
These pages are out of scope for this project, but they should be available in the navigation solution.

Please submit your initial design concepts, accompanied by a brief explanation of your approach and the rationale behind your design choices. We will offer feedback and collaborate with the chosen designer to refine the design, ensuring it meets our requirements and vision.

We are really hoping to see some elegant user interfaces. The functionality describe in the attachment is important, but the layout is not. Feel free to invent.

Attached files:

Target Market(s)

Energy intensive industries

Requirements
Must have
• Easy to navigate through the different data dimensions: Time, assets, mitigation measures, and advanced details under mitigation measures. The design in the attached files are just our working drafts. Creative alternatives are very welcome.
Nice to have
• Elegant layouts that differ from our working drafts.

```html
<!DOCTYPE html>
<html lang="en">
<head>
<meta charset="utf-8">
<title>Brelmont KORVa – Work Bench</title>
<link href="https://fonts.googleapis.com/css2?family=Lexend:wght@300;400;500;600&display=swap" rel="stylesheet">
<style>
:root{
  --canvas:#8b8b8b;
  --page:#e9ecf6;
  --white:#ffffff;
  --ink:#1d2433;
  --muted:#6b7385;
  --brand:#2f6f9a;
  --side-top:#4d8a8c;
  --side-bottom:#1c5a98;
  --teal:#4e8f90;
  --orange:#e07c5c;
  --red:#e4574a;
  --yellow:#e8c33a;
  --navy:#2e5590;
  --blue:#3a6fd8;
  --green:#7cc07d;
  --purple:#8a4fe0;
  --line:#e2563f;
  --tick:#9aa3b5;
  --mini:#7f9fd6;
}
*{box-sizing:border-box;margin:0;padding:0}
html,body{width:1200px;height:4202px;overflow:hidden;background:var(--canvas);font-family:"Lexend",sans-serif;color:var(--ink)}
.screen{position:absolute;left:41px;width:1118px;background:var(--page);overflow:hidden}
.topbar{position:absolute;left:0;top:0;width:100%;height:40px;background:var(--white)}
.brand{position:absolute;left:20px;top:9px;font-size:19px;font-weight:500;color:var(--brand);letter-spacing:1px}
.avatar{position:absolute;right:18px;top:6px;width:28px;height:28px;border-radius:50%;background:linear-gradient(135deg,#8c8f96,#4b4f57)}
.avatar::after{content:"";position:absolute;right:-1px;top:1px;width:7px;height:7px;border-radius:50%;background:#3cc45a;border:1px solid #fff}
.sidebar{position:absolute;left:0;top:40px;bottom:0;width:184px;background:linear-gradient(180deg,var(--side-top),var(--side-bottom))}
.search{position:absolute;left:0;top:6px;width:184px;height:22px;border-bottom:1px solid rgba(255,255,255,.5);color:#fff;font-size:8.5px;padding:6px 14px}
.search svg{position:absolute;right:16px;top:6px}
.nav-group{position:absolute;left:16px;color:#fff;font-size:9px;font-weight:600}
.nav-item{position:absolute;left:18px;color:#fff;font-size:7.5px;font-weight:300;width:166px;height:15px;line-height:15px}
.nav-item.active{background:#fff;color:var(--brand);left:0;padding-left:18px}
.chev{position:absolute;left:176px;width:15px;height:15px;border-radius:50%;background:#fff;box-shadow:0 1px 3px rgba(0,0,0,.2)}
.chev svg{position:absolute;left:3px;top:3px}
.card{position:absolute;background:var(--white);border-radius:14px;box-shadow:0 2px 8px rgba(40,60,110,.08)}
.card-empty{display:flex;align-items:center;justify-content:center;font-size:17px;font-weight:500}
.card-title{position:absolute;left:0;right:0;text-align:center;font-size:17px;font-weight:500}
.chart-card svg{position:absolute;left:30px;top:70px}
.form-sub{position:absolute;font-size:13px;color:var(--brand);font-weight:400}
.filters{position:absolute;left:14px;top:85px;font-size:8.5px;font-weight:500;display:flex;gap:4px;align-items:center}
.chip{background:var(--teal);color:#fff;font-size:6px;padding:2px 5px;border-radius:2px;font-weight:400}
.asset-table{position:absolute;left:14px;top:102px;width:250px;font-size:6px;font-weight:300;border-collapse:collapse}
.asset-table td,.asset-table th{height:18px;font-weight:300;text-align:left;padding:0 2px;white-space:nowrap}
.asset-table th{height:14px;font-size:5.5px}
.box{display:inline-block;width:7px;height:7px;border:1px solid #c9cfdb}
.box.on{background:var(--navy);border-color:var(--navy)}
.param-label{position:absolute;left:302px;font-size:8.5px}
.param-input{position:absolute;left:364px;width:68px;height:18px;border:1px solid #dfe3ec;border-radius:3px;font-size:6.5px;padding:5px 8px;box-shadow:0 1px 3px rgba(0,0,0,.05)}
.param-dot{position:absolute;left:394px;width:6px;height:6px;background:var(--navy)}
.insert{position:absolute;left:210px;top:270px;width:44px;height:14px;background:var(--teal);color:#fff;border-radius:3px;font-size:6.5px;text-align:center;line-height:14px}
.dates{position:absolute;left:0;width:100%;font-size:8px;color:#333}
.dates span{position:absolute;transform:translateX(-50%)}
.controls{position:absolute;left:207px;display:flex;gap:2px;align-items:center}
.ctrl{width:12px;height:12px;border-radius:2px;background:#dfe3ec;font-size:6px;text-align:center;line-height:12px;color:#555}
.ctrl.play{background:var(--navy);color:#fff}
.current{position:absolute;left:261px;font-size:8px}
.ticks{position:absolute;left:334px;width:763px;height:7px;border-bottom:1px solid var(--tick);background:repeating-linear-gradient(90deg,var(--tick) 0 1px,transparent 1px 8px)}
.cursor{position:absolute;left:430px;width:1px;background:var(--line)}
.cursor::before{content:"";position:absolute;left:-3px;top:-3px;width:7px;height:7px;border-radius:50%;background:var(--line)}
.minimap{position:absolute;left:334px}
.lane{position:absolute;left:204px;width:895px;height:38px;background:var(--white)}
.bar{position:absolute;height:38px;color:#fff;padding:6px 30px;font-size:11px}
.bar small{display:block;font-size:7px;opacity:.85;margin-top:1px}
.bar svg{position:absolute;right:12px;top:9px}
.banner{position:absolute;left:204px;width:895px;height:37px;background:var(--yellow);color:#fff;font-size:17px;text-align:center;line-height:37px}
.banner small{position:absolute;right:40px;font-size:7.5px}
.banner svg{position:absolute;right:16px;top:9px}
.field-lane{position:absolute;left:204px;width:895px;height:24px;background:var(--white)}
.field{position:absolute;height:24px;color:#fff;font-size:9px;text-align:center;line-height:24px}
</style>
</head>
<body>
<svg width="0" height="0" style="position:absolute">
  <defs>
    <symbol id="chart-two" viewBox="0 0 340 180">
      <rect x="30" y="6" width="150" height="140" fill="#eef0f6"/>
      <g font-size="5" fill="#888" font-family="Lexend,sans-serif">
        <text x="10" y="10">175</text><text x="10" y="30">150</text><text x="10" y="50">125</text><text x="10" y="70">100</text><text x="14" y="90">75</text><text x="14" y="110">50</text><text x="14" y="130">25</text><text x="18" y="148">0</text>
        <text x="35" y="156">1995</text><text x="60" y="156">2000</text><text x="85" y="156">2005</text><text x="110" y="156">2010</text><text x="135" y="156">2015</text><text x="160" y="156">2020</text><text x="185" y="156">2025</text><text x="210" y="156">2030</text><text x="235" y="156">2035</text><text x="260" y="156">2040</text><text x="285" y="156">2045</text><text x="305" y="156">2050</text>
        <text x="130" y="168">— Corporate average</text><text x="200" y="168">— Corporate goals</text>
      </g>
      <path d="M50 130 L55 124 58 128 62 118 66 122 70 110 74 116 78 104 82 112 86 100 90 108 94 96 98 104 100 80 103 100 107 92 110 60 113 96 117 84 120 50 123 88 127 76 130 94 134 82 138 96 142 86 146 98 150 90 156 96 162 88 168 96 174 92 180 100" fill="none" stroke="#e9886a" stroke-width="1"/>
      <path d="M180 100 L205 92 230 86 240 74 255 70 260 58 275 54 285 42 300 36 310 24 320 14" fill="none" stroke="#e9886a" stroke-width="1"/>
      <path d="M180 100 L210 115 240 125 270 132 300 138 320 144" fill="none" stroke="#3c7a86" stroke-width="1"/>
    </symbol>
    <symbol id="chart-three" viewBox="0 0 340 180">
      <use href="#chart-two"/>
      <path d="M180 100 L195 108 205 102 215 112 225 106 235 118 245 112 255 122 265 116 280 126 295 122 310 130 320 128" fill="none" stroke="#4d7fd1" stroke-width="1"/>
      <text x="260" y="168" font-size="5" fill="#888" font-family="Lexend,sans-serif">— Savings incl. measure</text>
    </symbol>
    <symbol id="mini" viewBox="0 0 763 28" preserveAspectRatio="none">
      <rect x="228" y="0" width="230" height="28" fill="#8fa7cf" opacity=".55"/>
      <path d="M0 20 L40 18 80 21 120 16 160 19 200 14 240 17 280 12 320 15 360 8 400 13 440 10 480 15 520 11 560 16 600 13 640 17 680 12 720 16 763 14 L763 28 0 28Z" fill="var(--mini)"/>
      <line x1="0" y1="1" x2="763" y2="1" stroke="#555" stroke-width="1"/>
    </symbol>
    <symbol id="updown" viewBox="0 0 10 20"><path d="M5 1V19M1 5L5 1 9 5M1 15L5 19 9 15" fill="none" stroke="#fff" stroke-width="1.3"/></symbol>
    <symbol id="chev-l" viewBox="0 0 9 9"><path d="M6 1L2.5 4.5 6 8" fill="none" stroke="#2f6f9a" stroke-width="1.4"/></symbol>
    <symbol id="chev-d" viewBox="0 0 9 9"><path d="M1 3L4.5 6.5 8 3" fill="none" stroke="#2f6f9a" stroke-width="1.4"/></symbol>
  </defs>
</svg>

<!-- ===== Screen 1 ===== -->
<section class="screen" style="top:36px;height:740px">
  <header class="topbar"><div class="brand">Brelmont</div><div class="avatar" role="img" aria-label="User profile photo"></div></header>
  <nav class="sidebar">
    <div class="search">Search<svg width="9" height="9" viewBox="0 0 10 10"><circle cx="4" cy="4" r="3" fill="none" stroke="#fff"/><path d="M6.5 6.5L9 9" stroke="#fff"/></svg></div>
    <div class="nav-group" style="top:76px">Switch Energy Carrier</div><div class="chev" style="top:74px"><svg width="9" height="9"><use href="#chev-l"/></svg></div>
    <div class="nav-group" style="top:104px">Energy Efficiency Measures</div><div class="chev" style="top:102px"><svg width="9" height="9"><use href="#chev-d"/></svg></div>
    <div class="nav-item" style="top:124px">Venting To Flare</div>
    <div class="nav-item" style="top:145px">Venting To Production</div>
    <div class="nav-item" style="top:166px">Fugitive Emissions Measure</div>
    <div class="nav-item" style="top:187px">Compressor Replacement</div>
    <div class="nav-item" style="top:208px">Reduced Water Injection</div>
    <div class="nav-item" style="top:229px">Drilling Improvements</div>
    <div class="nav-group" style="top:266px">Ending Of Pipe Measures</div><div class="chev" style="top:264px"><svg width="9" height="9"><use href="#chev-l"/></svg></div>
    <div class="nav-group" style="top:291px">Company Structure</div><div class="chev" style="top:289px"><svg width="9" height="9"><use href="#chev-d"/></svg></div>
    <div class="nav-item" style="top:308px">Change End Of Life</div>
    <div class="nav-item" style="top:329px">New Net Zero Assets</div>
    <div class="nav-item" style="top:350px">Update License OwnerShips</div>
  </nav>
  <div class="card card-empty" style="left:204px;top:65px;width:463px;height:279px">Select A Mitigation Measure</div>
  <div class="card chart-card" style="left:698px;top:65px;width:401px;height:279px"><div class="card-title" style="top:30px">Predicted Specific CO2 Emissions</div><svg width="340" height="180"><use href="#chart-two"/></svg></div>
  <div class="dates" style="top:373px"><span style="left:429px">January 2023</span><span style="left:530px">July 2023</span><span style="left:632px">January 2023</span><span style="left:733px">July 2023</span><span style="left:834px">January 2023</span><span style="left:935px">July 2023</span><span style="left:1036px">January 2023</span></div>
  <div class="controls" style="top:396px"><div class="ctrl">«</div><div class="ctrl play">▶</div><div class="ctrl">»</div></div>
  <div class="current" style="top:398px">January 2023</div>
  <div class="ticks" style="top:397px"></div>
  <div class="cursor" style="top:400px;height:268px"></div>
  <svg class="minimap" style="top:676px" width="763" height="28"><use href="#mini"/></svg>
</section>

<!-- ===== Screen 2 ===== -->
<section class="screen" style="top:828px;height:742px">
  <header class="topbar"><div class="brand">Brelmont</div><div class="avatar" role="img" aria-label="User profile photo"></div></header>
  <nav class="sidebar">
    <div class="search">Search<svg width="9" height="9" viewBox="0 0 10 10"><circle cx="4" cy="4" r="3" fill="none" stroke="#fff"/><path d="M6.5 6.5L9 9" stroke="#fff"/></svg></div>
    <div class="nav-group" style="top:76px">Switch Energy Carrier</div><div class="chev" style="top:74px"><svg width="9" height="9"><use href="#chev-l"/></svg></div>
    <div class="nav-group" style="top:104px">Energy Efficiency Measures</div><div class="chev" style="top:102px"><svg width="9" height="9"><use href="#chev-d"/></svg></div>
    <div class="nav-item" style="top:124px">Venting To Flare</div>
    <div class="nav-item" style="top:145px">Venting To Production</div>
    <div class="nav-item" style="top:166px">Fugitive Emissions Measure</div>
    <div class="nav-item active" style="top:187px">Compressor Replacement</div>
    <div class="nav-item" style="top:208px">Reduced Water Injection</div>
    <div class="nav-item" style="top:229px">Drilling Improvements</div>
    <div class="nav-group" style="top:266px">Ending Of Pipe Measures</div><div class="chev" style="top:264px"><svg width="9" height="9"><use href="#chev-l"/></svg></div>
    <div class="nav-group" style="top:291px">Company Structure</div><div class="chev" style="top:289px"><svg width="9" height="9"><use href="#chev-d"/></svg></div>
    <div class="nav-item" style="top:308px">Change End Of Life</div>
    <div class="nav-item" style="top:329px">New Net Zero Assets</div>
    <div class="nav-item" style="top:350px">Update License OwnerShips</div>
  </nav>
  <div class="card" style="left:204px;top:65px;width:463px;height:279px">
    <div class="card-title" style="top:18px">Compressor Rebundling</div>
    <div class="form-sub" style="left:80px;top:54px">Assets</div>
    <div class="form-sub" style="left:317px;top:54px">Parameters</div>
    <div class="filters">Active filters <span class="chip">Lorem ipsu</span><span class="chip">Lorem ipsu</span><span class="chip">Lorem ipsu</span></div>
    <table class="asset-table">
      <tr><th>Escap ▽</th><th>Escap ▽</th><th>Escap ▽</th><th>Escap ▽</th><th>Escap ▽</th><th>Escap ▽</th><th></th></tr>
      <tr><td>Lorem ipsum</td><td>Lorem</td><td>Lorem ipsum</td><td>Lorem ipsum</td><td>100%</td><td>Lorem</td><td><span class="box"></span></td></tr>
      <tr><td>Lorem ipsum</td><td>Lorem</td><td>Lorem ipsum</td><td>Lorem ipsum</td><td>100%</td><td>Lorem</td><td><span class="box on"></span></td></tr>
      <tr><td>Lorem ipsum</td><td>Lorem</td><td>Lorem ipsum</td><td>Lorem ipsum</td><td>100%</td><td>Lorem</td><td><span class="box"></span></td></tr>
      <tr><td>Lorem ipsum</td><td>Lorem</td><td>Lorem ipsum</td><td>Lorem ipsum</td><td>100%</td><td>Lorem</td><td><span class="box on"></span></td></tr>
      <tr><td>Lorem ipsum</td><td>Lorem</td><td>Lorem ipsum</td><td>Lorem ipsum</td><td>100%</td><td>Lorem</td><td><span class="box"></span></td></tr>
      <tr><td>Lorem ipsum</td><td>Lorem</td><td>Lorem ipsum</td><td>Lorem ipsum</td><td>100%</td><td>Lorem</td><td><span class="box"></span></td></tr>
      <tr><td>Lorem ipsum</td><td>Lorem</td><td>Lorem ipsum</td><td>Lorem ipsum</td><td>100%</td><td>Lorem</td><td><span class="box on"></span></td></tr>
      <tr><td>Lorem ipsum</td><td>Lorem</td><td>Lorem ipsum</td><td>Lorem ipsum</td><td>100%</td><td>Lorem</td><td><span class="box"></span></td></tr>
    </table>
    <div class="insert">Insert</div>
    <div class="param-label" style="top:108px">Start</div><div class="param-input" style="top:102px">January 2023</div>
    <div class="param-label" style="top:138px">End</div><div class="param-input" style="top:132px">October 2024</div>
    <div class="param-label" style="top:168px">Duration</div><div class="param-input" style="top:162px">21 months</div>
    <div class="param-label" style="top:198px">Factor</div><div class="param-input" style="top:192px">2x</div>
    <div class="param-label" style="top:228px">Jalla Jall</div><div class="param-dot" style="top:230px"></div>
  </div>
  <div class="card chart-card" style="left:698px;top:65px;width:401px;height:279px"><div class="card-title" style="top:30px">Predicted Specific CO2 Emissions</div><svg width="340" height="180"><use href="#chart-two"/></svg></div>
  <div class="dates" style="top:387px"><span style="left:429px">January 2023</span><span style="left:530px">July 2023</span><span style="left:632px">January 2023</span><span style="left:733px">July 2023</span><span style="left:834px">January 2023</span><span style="left:935px">July 2023</span><span style="left:1036px">January 2023</span></div>
  <div class="controls" style="top:410px"><div class="ctrl">«</div><div class="ctrl play">▶</div><div class="ctrl">»</div></div>
  <div class="current" style="top:412px">January 2023</div>
  <div class="ticks" style="top:411px"></div>
  <div class="cursor" style="top:414px;height:266px"></div>
  <svg class="minimap" style="top:690px" width="763" height="28"><use href="#mini"/></svg>
</section>

<!-- ===== Screen 3 ===== -->
<section class="screen" style="top:1634px;height:740px">
  <header class="topbar"><div class="brand">Brelmont</div><div class="avatar" role="img" aria-label="User profile photo"></div></header>
  <nav class="sidebar">
    <div class="search">Search<svg width="9" height="9" viewBox="0 0 10 10"><circle cx="4" cy="4" r="3" fill="none" stroke="#fff"/><path d="M6.5 6.5L9 9" stroke="#fff"/></svg></div>
    <div class="nav-group" style="top:76px">Switch Energy Carrier</div><div class="chev" style="top:74px"><svg width="9" height="9"><use href="#chev-l"/></svg></div>
    <div class="nav-group" style="top:104px">Energy Efficiency Measures</div><div class="chev" style="top:102px"><svg width="9" height="9"><use href="#chev-d"/></svg></div>
    <div class="nav-item" style="top:124px">Venting To Flare</div>
    <div class="nav-item" style="top:145px">Venting To Production</div>
    <div class="nav-item" style="top:166px">Fugitive Emissions Measure</div>
    <div class="nav-item" style="top:187px">Compressor Replacement</div>
    <div class="nav-item" style="top:208px">Reduced Water Injection</div>
    <div class="nav-item" style="top:229px">Drilling Improvements</div>
    <div class="nav-group" style="top:266px">Ending Of Pipe Measures</div><div class="chev" style="top:264px"><svg width="9" height="9"><use href="#chev-l"/></svg></div>
    <div class="nav-group" style="top:291px">Company Structure</div><div class="chev" style="top:289px"><svg width="9" height="9"><use href="#chev-d"/></svg></div>
    <div class="nav-item" style="top:308px">Change End Of Life</div>
    <div class="nav-item" style="top:329px">New Net Zero Assets</div>
    <div class="nav-item" style="top:350px">Update License OwnerShips</div>
  </nav>
  <div class="card" style="left:204px;top:65px;width:463px;height:279px">
    <div class="card-title" style="top:18px">Compressor Replacement</div>
    <div class="form-sub" style="left:80px;top:54px">Assets</div>
    <div class="form-sub" style="left:317px;top:54px">Parameters</div>
    <div class="filters">Active filters <span class="chip">Lorem ipsu</span><span class="chip">Lorem ipsu</span><span class="chip">Lorem ipsu</span></div>
    <table class="asset-table">
      <tr><th>Escap ▽</th><th>Escap ▽</th><th>Escap ▽</th><th>Escap ▽</th><th>Escap ▽</th><th>Escap ▽</th><th></th></tr>
      <tr><td>Lorem ipsum</td><td>Lorem</td><td>Lorem ipsum</td><td>Lorem ipsum</td><td>100%</td><td>Lorem</td><td><span class="box"></span></td></tr>
      <tr><td>Lorem ipsum</td><td>Lorem</td><td>Lorem ipsum</td><td>Lorem ipsum</td><td>100%</td><td>Lorem</td><td><span class="box on"></span></td></tr>
      <tr><td>Lorem ipsum</td><td>Lorem</td><td>Lorem ipsum</td><td>Lorem ipsum</td><td>100%</td><td>Lorem</td><td><span class="box"></span></td></tr>
      <tr><td>Lorem ipsum</td><td>Lorem</td><td>Lorem ipsum</td><td>Lorem ipsum</td><td>100%</td><td>Lorem</td><td><span class="box on"></span></td></tr>
      <tr><td>Lorem ipsum</td><td>Lorem</td><td>Lorem ipsum</td><td>Lorem ipsum</td><td>100%</td><td>Lorem</td><td><span class="box"></span></td></tr>
      <tr><td>Lorem ipsum</td><td>Lorem</td><td>Lorem ipsum</td><td>Lorem ipsum</td><td>100%</td><td>Lorem</td><td><span class="box"></span></td></tr>
      <tr><td>Lorem ipsum</td><td>Lorem</td><td>Lorem ipsum</td><td>Lorem ipsum</td><td>100%</td><td>Lorem</td><td><span class="box on"></span></td></tr>
      <tr><td>Lorem ipsum</td><td>Lorem</td><td>Lorem ipsum</td><td>Lorem ipsum</td><td>100%</td><td>Lorem</td><td><span class="box"></span></td></tr>
    </table>
    <div class="param-label" style="top:108px">Start</div><div class="param-input" style="top:102px">January 2023</div>
    <div class="param-label" style="top:138px">End</div><div class="param-input" style="top:132px">October 2024</div>
    <div class="param-label" style="top:168px">Duration</div><div class="param-input" style="top:162px">21 months</div>
    <div class="param-label" style="top:198px">Factor</div><div class="param-input" style="top:192px">2x</div>
    <div class="param-label" style="top:228px">Jalla Jall</div><div class="param-dot" style="top:230px"></div>
  </div>
  <div class="card chart-card" style="left:698px;top:65px;width:401px;height:279px"><div class="card-title" style="top:30px">Predicted Specific CO2 Emissions</div><svg width="340" height="180"><use href="#chart-three"/></svg></div>
  <div class="dates" style="top:382px"><span style="left:429px">January 2023</span><span style="left:530px">July 2023</span><span style="left:632px">January 2023</span><span style="left:733px">July 2023</span><span style="left:834px">January 2023</span><span style="left:935px">July 2023</span><span style="left:1036px">January 2023</span></div>
  <div class="controls" style="top:405px"><div class="ctrl">«</div><div class="ctrl play">▶</div><div class="ctrl">»</div></div>
  <div class="current" style="top:407px">January 2023</div>
  <div class="ticks" style="top:406px"></div>
  <div class="lane" style="top:527px"></div>
  <div class="bar" style="left:432px;top:527px;width:279px;background:var(--teal)">Compressor rebundling<small>3/10 Assets Included</small><svg width="10" height="20"><use href="#updown"/></svg></div>
  <svg class="minimap" style="top:686px" width="763" height="28"><use href="#mini"/></svg>
</section>

<!-- ===== Screen 4 ===== -->
<section class="screen" style="top:2431px;height:740px">
  <header class="topbar"><div class="brand">Brelmont</div><div class="avatar" role="img" aria-label="User profile photo"></div></header>
  <nav class="sidebar">
    <div class="search">Search<svg width="9" height="9" viewBox="0 0 10 10"><circle cx="4" cy="4" r="3" fill="none" stroke="#fff"/><path d="M6.5 6.5L9 9" stroke="#fff"/></svg></div>
    <div class="nav-group" style="top:76px">Switch Energy Carrier</div><div class="chev" style="top:74px"><svg width="9" height="9"><use href="#chev-l"/></svg></div>
    <div class="nav-group" style="top:104px">Energy Efficiency Measures</div><div class="chev" style="top:102px"><svg width="9" height="9"><use href="#chev-d"/></svg></div>
    <div class="nav-item" style="top:124px">Venting To Flare</div>
    <div class="nav-item" style="top:145px">Venting To Production</div>
    <div class="nav-item" style="top:166px">Fugitive Emissions Measure</div>
    <div class="nav-item" style="top:187px">Compressor Replacement</div>
    <div class="nav-item" style="top:208px">Reduced Water Injection</div>
    <div class="nav-item" style="top:229px">Drilling Improvements</div>
    <div class="nav-group" style="top:266px">Ending Of Pipe Measures</div><div class="chev" style="top:264px"><svg width="9" height="9"><use href="#chev-l"/></svg></div>
    <div class="nav-group" style="top:291px">Company Structure</div><div class="chev" style="top:289px"><svg width="9" height="9"><use href="#chev-d"/></svg></div>
    <div class="nav-item" style="top:308px">Change End Of Life</div>
    <div class="nav-item" style="top:329px">New Net Zero Assets</div>
    <div class="nav-item" style="top:350px">Update License OwnerShips</div>
  </nav>
  <div class="card card-empty" style="left:204px;top:65px;width:463px;height:279px">Select A Mitigation Measure</div>
  <div class="card chart-card" style="left:698px;top:65px;width:401px;height:279px"><div class="card-title" style="top:30px">Predicted Specific CO2 Emissions</div><svg width="340" height="180"><use href="#chart-three"/></svg></div>
  <div class="dates" style="top:382px"><span style="left:429px">January 2023</span><span style="left:530px">July 2023</span><span style="left:632px">January 2023</span><span style="left:733px">July 2023</span><span style="left:834px">January 2023</span><span style="left:935px">July 2023</span><span style="left:1036px">January 2023</span></div>
  <div class="controls" style="top:405px"><div class="ctrl">«</div><div class="ctrl play">▶</div><div class="ctrl">»</div></div>
  <div class="current" style="top:407px">January 2023</div>
  <div class="ticks" style="top:406px"></div>
  <div class="lane" style="top:468px"></div>
  <div class="lane" style="top:515px"></div>
  <div class="lane" style="top:562px"></div>
  <div class="lane" style="top:609px"></div>
  <div class="bar" style="left:430px;top:468px;width:281px;background:var(--teal)">Compressor rebundling<small>3/10 Assets Included</small><svg width="10" height="20"><use href="#updown"/></svg></div>
  <div class="bar" style="left:711px;top:515px;width:280px;background:var(--orange)">Optimize gas lift<small>5/10 Assets Included</small><svg width="10" height="20"><use href="#updown"/></svg></div>
  <div class="bar" style="left:430px;top:562px;width:437px;background:var(--yellow)">Power from shore<small>7/10 Assets Included</small><svg width="10" height="20"><use href="#updown"/></svg></div>
  <div class="bar" style="left:430px;top:609px;width:437px;background:var(--navy)">Reduced flaring<small>1/10 Assets Included</small><svg width="10" height="20"><use href="#updown"/></svg></div>
  <div class="cursor" style="top:409px;height:300px"></div>
  <svg class="minimap" style="top:686px" width="763" height="28"><use href="#mini"/></svg>
</section>

<!-- ===== Screen 5 ===== -->
<section class="screen" style="top:3220px;height:926px">
  <header class="topbar"><div class="brand">Brelmont</div><div class="avatar" role="img" aria-label="User profile photo"></div></header>
  <nav class="sidebar">
    <div class="search">Search<svg width="9" height="9" viewBox="0 0 10 10"><circle cx="4" cy="4" r="3" fill="none" stroke="#fff"/><path d="M6.5 6.5L9 9" stroke="#fff"/></svg></div>
    <div class="nav-group" style="top:76px">Switch Energy Carrier</div><div class="chev" style="top:74px"><svg width="9" height="9"><use href="#chev-l"/></svg></div>
    <div class="nav-group" style="top:104px">Energy Efficiency Measures</div><div class="chev" style="top:102px"><svg width="9" height="9"><use href="#chev-d"/></svg></div>
    <div class="nav-item" style="top:124px">Venting To Flare</div>
    <div class="nav-item" style="top:145px">Venting To Production</div>
    <div class="nav-item" style="top:166px">Fugitive Emissions Measure</div>
    <div class="nav-item" style="top:187px">Compressor Replacement</div>
    <div class="nav-item" style="top:208px">Reduced Water Injection</div>
    <div class="nav-item" style="top:229px">Drilling Improvements</div>
    <div class="nav-group" style="top:266px">Ending Of Pipe Measures</div><div class="chev" style="top:264px"><svg width="9" height="9"><use href="#chev-l"/></svg></div>
    <div class="nav-group" style="top:291px">Company Structure</div><div class="chev" style="top:289px"><svg width="9" height="9"><use href="#chev-d"/></svg></div>
    <div class="nav-item" style="top:308px">Change End Of Life</div>
    <div class="nav-item" style="top:329px">New Net Zero Assets</div>
    <div class="nav-item" style="top:350px">Update License OwnerShips</div>
  </nav>
  <div class="card" style="left:204px;top:65px;width:463px;height:297px">
    <div class="card-title" style="top:18px">Power from shore</div>
    <div class="form-sub" style="left:80px;top:54px">Assets</div>
    <div class="form-sub" style="left:317px;top:54px">Parameters</div>
    <div class="filters">Active filters <span class="chip">Lorem ipsu</span><span class="chip">Lorem ipsu</span><span class="chip">Lorem ipsu</span></div>
    <table class="asset-table">
      <tr><th>Escap ▽</th><th>Escap ▽</th><th>Escap ▽</th><th>Escap ▽</th><th>Escap ▽</th><th>Escap ▽</th><th></th></tr>
      <tr><td>Lorem ipsum</td><td>Lorem</td><td>Lorem ipsum</td><td>Lorem ipsum</td><td>100%</td><td>Lorem</td><td><span class="box on"></span></td></tr>
      <tr><td>Lorem ipsum</td><td>Lorem</td><td>Lorem ipsum</td><td>Lorem ipsum</td><td>100%</td><td>Lorem</td><td><span class="box on"></span></td></tr>
      <tr><td>Lorem ipsum</td><td>Lorem</td><td>Lorem ipsum</td><td>Lorem ipsum</td><td>100%</td><td>Lorem</td><td><span class="box on"></span></td></tr>
      <tr><td>Lorem ipsum</td><td>Lorem</td><td>Lorem ipsum</td><td>Lorem ipsum</td><td>100%</td><td>Lorem</td><td><span class="box on"></span></td></tr>
      <tr><td>Lorem ipsum</td><td>Lorem</td><td>Lorem ipsum</td><td>Lorem ipsum</td><td>100%</td><td>Lorem</td><td><span class="box on"></span></td></tr>
      <tr><td>Lorem ipsum</td><td>Lorem</td><td>Lorem ipsum</td><td>Lorem ipsum</td><td>100%</td><td>Lorem</td><td><span class="box"></span></td></tr>
      <tr><td>Lorem ipsum</td><td>Lorem</td><td>Lorem ipsum</td><td>Lorem ipsum</td><td>100%</td><td>Lorem</td><td><span class="box on"></span></td></tr>
      <tr><td>Lorem ipsum</td><td>Lorem</td><td>Lorem ipsum</td><td>Lorem ipsum</td><td>100%</td><td>Lorem</td><td><span class="box"></span></td></tr>
    </table>
    <div class="param-label" style="top:108px">Start</div><div class="param-input" style="top:102px">January 2023</div>
    <div class="param-label" style="top:138px">End</div><div class="param-input" style="top:132px">October 2024</div>
    <div class="param-label" style="top:168px">Duration</div><div class="param-input" style="top:162px">21 months</div>
    <div class="param-label" style="top:198px">Factor</div><div class="param-input" style="top:192px">2x</div>
    <div class="param-label" style="top:228px">Jalla Jall</div><div class="param-dot" style="top:230px"></div>
  </div>
  <div class="card chart-card" style="left:698px;top:65px;width:401px;height:279px"><div class="card-title" style="top:30px">Predicted Specific CO2 Emissions</div><svg width="340" height="180"><use href="#chart-three"/></svg></div>
  <div class="banner" style="top:395px">Power from shore<small>7/10 Assets Included</small><svg width="10" height="20"><use href="#updown"/></svg></div>
  <div class="dates" style="top:449px"><span style="left:429px">January 2023</span><span style="left:530px">July 2023</span><span style="left:632px">January 2023</span><span style="left:733px">July 2023</span><span style="left:834px">January 2023</span><span style="left:935px">July 2023</span><span style="left:1036px">January 2023</span></div>
  <div class="controls" style="top:472px"><div class="ctrl">«</div><div class="ctrl play">▶</div><div class="ctrl">»</div></div>
  <div class="current" style="top:474px">January 2023</div>
  <div class="ticks" style="top:473px"></div>
  <div class="field-lane" style="top:500px"></div><div class="field" style="left:685px;top:500px;width:275px;background:var(--red)">DEMO FIELD 1</div>
  <div class="field-lane" style="top:534px"></div><div class="field" style="left:540px;top:534px;width:348px;background:var(--orange)">DEMO FIELD 2</div>
  <div class="field-lane" style="top:568px"></div><div class="field" style="left:540px;top:568px;width:348px;background:var(--green)">DEMO FIELD 3</div>
  <div class="field-lane" style="top:602px"></div><div class="field" style="left:624px;top:602px;width:411px;background:var(--yellow)">DEMO FIELD 4</div>
  <div class="field-lane" style="top:636px"></div><div class="field" style="left:522px;top:636px;width:280px;background:var(--blue)">DEMO FIELD 5</div>
  <div class="field-lane" style="top:670px"></div><div class="field" style="left:685px;top:670px;width:189px;background:var(--navy)">DEMO FIELD 6</div>
  <div class="field-lane" style="top:704px"></div><div class="field" style="left:685px;top:704px;width:189px;background:var(--purple)">DEMO FIELD 7</div>
  <div class="cursor" style="top:476px;height:432px"></div>
  <svg class="minimap" style="top:886px" width="763" height="28"><use href="#mini"/></svg>
</section>
</body>
</html>
```